Health Care Company with Logo Needs Business Cards designed

We are a luxury behavioral health company looking for business cards design we already have a logo and are looking for someone to design a sophisticated luxurious looking business card. Please note that Card design should be captivating just like the logo and also encompass the logo color

Industry/Entity Type

Healthcare

Contact Information for Business Card

Logo,company name, tagline, my name and title, contact details, and physical address

```html
<!DOCTYPE html>
<html lang="en">
<head>
<meta charset="utf-8">
<title>Marlow Behavioral Health – Business Cards</title>
<link rel="stylesheet" href="https://fonts.googleapis.com/css2?family=Open+Sans:wght@400;700&display=swap">
<style>
  :root{
    --bg:#2a2a2b;
    --card:#f7f7f7;
    --card-shade:#ececec;
    --purple:#6f2f91;
    --blue:#1b9ad6;
    --green:#7cb82f;
    --orange:#e8880f;
    --ink:#4a4a4a;
    --muted:#6b6b6b;
  }
  *{box-sizing:border-box;margin:0;padding:0}
  html,body{width:1200px;height:900px;overflow:hidden;background:var(--bg)}
  .canvas{position:relative;width:1200px;height:900px;background:var(--bg)}
  .card{
    position:absolute;width:620px;height:354px;overflow:hidden;
    background:linear-gradient(150deg,var(--card-shade) 0%,var(--card) 55%,#fff 100%);
    box-shadow:0 14px 30px rgba(0,0,0,.55);
    font-family:"Open Sans",sans-serif;
  }
  .card--front{left:60px;top:60px}
  .card--back{left:520px;top:486px}

  .brand{display:flex;align-items:center;gap:12px;white-space:nowrap}
  .brand__mark{width:36px;height:36px;background:var(--purple);flex:none}
  .brand__name{
    font-family:"Open Sans",sans-serif;font-weight:700;
    color:var(--purple);font-size:27px;line-height:1.1;
  }
  .brand__tagline{
    font-family:"Open Sans",sans-serif;font-weight:400;
    color:var(--blue);font-size:12px;letter-spacing:1.6px;
    margin-top:4px;
  }

  /* front */
  .front__lockup{position:absolute;left:120px;top:120px}
  .front__web{
    position:absolute;left:168px;top:226px;white-space:nowrap;
    color:var(--green);font-size:16px;letter-spacing:3.5px;
  }
  .front__rule{position:absolute;left:110px;top:262px;width:440px;height:1px;background:var(--purple);opacity:.7}

  /* back */
  .person{position:absolute;left:44px;top:56px}
  .person__title{color:var(--muted);font-size:18px;line-height:1.1}
  .person__name{
    font-weight:700;color:var(--orange);font-size:24px;
    letter-spacing:1px;text-transform:uppercase;line-height:1.2
  }
  .contact{position:absolute;left:300px;top:40px;list-style:none;color:var(--ink);font-size:15.5px;white-space:nowrap}
  .contact__item{display:flex;align-items:flex-start;gap:10px;margin-bottom:8px;line-height:1.25}
  .contact__icon{width:16px;height:16px;flex:none;margin-top:2px}
  .back__rule{position:absolute;left:260px;top:218px;width:336px;height:1.5px;background:var(--green)}
  .back__lockup{position:absolute;left:240px;top:244px;gap:10px}
  .back__lockup .brand__name{font-size:22px}
  .back__lockup .brand__tagline{font-size:10.5px;letter-spacing:1.4px}
  .back__lockup .brand__mark{width:30px;height:30px}
</style>
</head>
<body>
<main class="canvas">

  <section class="card card--front" aria-label="Card front">
    <div class="front__lockup brand">
      <span class="brand__mark" aria-hidden="true"></span>
      <div>
        <div class="brand__name">Marlow Behavioral Health</div>
        <div class="brand__tagline">Calm care, steady support, new beginnings</div>
      </div>
    </div>
    <p class="front__web">www.marlowbehavioralhealth.com</p>
    <div class="front__rule"></div>
  </section>

  <section class="card card--back" aria-label="Card back">
    <div class="person">
      <p class="person__title">Director</p>
      <p class="person__name">John Smith</p>
    </div>

    <ul class="contact">
      <li class="contact__item">
        <svg class="contact__icon" viewBox="0 0 16 16" aria-hidden="true"><rect x="4" y="1" width="8" height="14" rx="1.5" fill="none" stroke="#1b9ad6" stroke-width="1.6"/><circle cx="8" cy="12.5" r="0.9" fill="#1b9ad6"/></svg>
        <span>0000 000 000</span>
      </li>
      <li class="contact__item">
        <svg class="contact__icon" viewBox="0 0 16 16" aria-hidden="true"><rect x="1" y="4" width="14" height="9" rx="1" fill="#1b9ad6"/><path d="M1.5 4.5 8 9.5l6.5-5" fill="none" stroke="#fff" stroke-width="1.2"/></svg>
        <span>john@marlowbehavioralhealth.com</span>
      </li>
      <li class="contact__item">
        <svg class="contact__icon" viewBox="0 0 16 16" aria-hidden="true"><circle cx="8" cy="8" r="6.5" fill="none" stroke="#1b9ad6" stroke-width="1.6"/><path d="M1.5 8h13M8 1.5c-3 3.5-3 9.5 0 13M8 1.5c3 3.5 3 9.5 0 13" fill="none" stroke="#1b9ad6" stroke-width="1.1"/></svg>
        <span>www.marlowbehavioralhealth.com</span>
      </li>
      <li class="contact__item">
        <svg class="contact__icon" viewBox="0 0 16 16" aria-hidden="true"><path d="M8 15s5-5.2 5-8.8A5 5 0 0 0 3 6.2C3 9.8 8 15 8 15z" fill="#1b9ad6"/><circle cx="8" cy="6.2" r="1.8" fill="#fff"/></svg>
        <span>11 dummy city, dummy place<br>P.O Box 0000 Dummy Land</span>
      </li>
    </ul>

    <div class="back__rule"></div>

    <div class="back__lockup brand">
      <span class="brand__mark" aria-hidden="true"></span>
      <div>
        <div class="brand__name">Marlow Behavioral Health</div>
        <div class="brand__tagline">Calm care, steady support, new beginnings</div>
      </div>
    </div>
  </section>

</main>
</body>
</html>
```